A-Frame Sign for CPR Training

Summit Readiness Academy provides CPR and First Aid classes to businesses and individuals throughout Northern California. We are in need of a 36in TALL x 24in WIDE poster insert to use on our A-Frame sign. We need the design to include:

1. our logo (see attachment)
2. a border (professional and clean, but catchy)
3. our contact information including phone #: 916-784-3126 and website: www.BlueRiverSkills.example
4. basic product info and price, possibly include a small picture for each?
"CPR - $39" and "BLS" - $49"
5. the phases: "CPR and First Aid Classes" and "Taught by Firefighters" and "Sacramento | Stockton | Modesto"
6. use our theme colors of blue(003399) and green(80cc33)
7. EXTRA CREDIT: somewhere place a small "camera" icon with the words "snap a picture of me for later"

Industry/Entity Type

Training

Font styles to use
Serif

Requirements
Nice to have
• EXTRA CREDIT: somewhere place a small "camera" icon with the words "snap a picture of me for later"

```html
<!DOCTYPE html>
<html lang="en">
<head>
<meta charset="utf-8">
<title>Summit Readiness Academy – A-Frame Sign</title>
<link href="https://fonts.googleapis.com/css2?family=Cinzel:wght@500;600&family=Oswald:wght@400;500;700&family=Quicksand:wght@400&family=Arimo:wght@400;700&family=Cormorant+Garamond:wght@500;600&display=swap" rel="stylesheet">
<style>
  :root {
    --brand-blue: #003399;
    --banner-blue: #1d42a0;
    --banner-blue-light: #2d53b0;
    --bar-blue: #5a7cc6;
    --brand-green: #80cc33;
    --tag-teal: #3fc3dc;
    --ring-teal: #3ab0cf;
    --ink: #141414;
    --ink-soft: #4a4a4a;
    --banner-text: #e6e6e6;
    --frame: #8c8c8c;
    --paper-a: #e2e3e6;
    --paper-b: #f2f2f3;
  }
  html, body { margin: 0; padding: 0; overflow: hidden; }
  body { width: 800px; height: 1200px; }
  .sign {
    position: relative;
    width: 800px;
    height: 1200px;
    overflow: hidden;
    background: linear-gradient(160deg, var(--paper-b) 0%, var(--paper-a) 45%, var(--paper-b) 70%, var(--paper-a) 100%);
  }
  .shapes { position: absolute; inset: 0; }
  .brand-name {
    position: absolute;
    left: 236px; top: 74px;
    margin: 0;
    font-family: "Cinzel", serif;
    font-weight: 600;
    color: var(--brand-blue);
    line-height: 1;
    white-space: nowrap;
  }
  .brand-name .line1 { display: block; font-size: 47px; letter-spacing: 1px; }
  .brand-name .line2 { display: block; font-size: 35px; letter-spacing: 3px; margin-top: 10px; }
  .tagline {
    position: absolute;
    left: 258px; top: 182px;
    margin: 0;
    font-family: "Cormorant Garamond", serif;
    font-weight: 500;
    font-size: 27px;
    letter-spacing: 8px;
    color: var(--ink-soft);
    white-space: nowrap;
  }
  .cities {
    position: absolute;
    left: 257px; top: 210px;
    margin: 0;
    font-family: "Cormorant Garamond", serif;
    font-weight: 600;
    font-size: 28px;
    letter-spacing: 4.4px;
    color: #2e2e2e;
    white-space: nowrap;
  }
  .banner-text {
    position: absolute;
    left: 46px;
    margin: 0;
    font-family: "Oswald", sans-serif;
    font-weight: 500;
    font-size: 54px;
    letter-spacing: 1px;
    color: var(--banner-text);
    line-height: 1;
    white-space: nowrap;
  }
  .banner-weekly { top: 290px; }
  .banner-firefighters { top: 402px; }
  .price-tag {
    position: absolute;
    margin: 0;
    font-family: "Oswald", sans-serif;
    font-weight: 700;
    font-size: 33px;
    letter-spacing: -0.5px;
    color: var(--ink);
    line-height: 68px;
    height: 68px;
    text-align: center;
    white-space: nowrap;
  }
  .price-bls { left: 272px; top: 560px; width: 142px; }
  .price-cpr { left: 476px; top: 916px; width: 144px; }
  .snap-note {
    position: absolute;
    left: 40px; top: 1078px;
    margin: 0;
    font-family: "Quicksand", sans-serif;
    font-size: 31px;
    line-height: 34px;
    color: #ffffff;
    white-space: nowrap;
  }
  .contact {
    position: absolute;
    left: 333px; top: 1097px;
    margin: 0;
    font-family: "Arimo", sans-serif;
    font-size: 20px;
    color: var(--ink);
    display: grid;
    grid-template-columns: 100px auto;
    row-gap: 6px;
    white-space: nowrap;
  }
  .contact dt { font-weight: 700; }
  .contact dd { margin: 0; letter-spacing: 0.8px; }
</style>
</head>
<body>
<main class="sign">
  <svg class="shapes" width="800" height="1200" viewBox="0 0 800 1200">
    <defs>
      <linearGradient id="banner-fill" x1="0" y1="0" x2="0" y2="1">
        <stop offset="0" stop-color="#2d53b0"/>
        <stop offset="1" stop-color="#1d42a0"/>
      </linearGradient>
      <radialGradient id="photo-aed" cx="0.5" cy="0.45" r="0.6">
        <stop offset="0" stop-color="#8a8680"/>
        <stop offset="1" stop-color="#4b4c50"/>
      </radialGradient>
      <radialGradient id="photo-cpr" cx="0.45" cy="0.4" r="0.6">
        <stop offset="0" stop-color="#9b7a63"/>
        <stop offset="1" stop-color="#5a5e66"/>
      </radialGradient>
    </defs>

    <rect class="frame-outer" x="5" y="5" width="790" height="1190" fill="none" stroke="var(--frame)" stroke-width="3"/>
    <rect class="frame-inner" x="13" y="13" width="774" height="1174" fill="none" stroke="var(--frame)" stroke-width="1.5"/>

    <circle class="brand-dot" cx="140" cy="128" r="62" fill="none" stroke="var(--brand-green)" stroke-width="5"/>

    <rect x="0" y="274" width="495" height="92" fill="url(#banner-fill)"/>
    <rect x="500" y="274" width="7" height="92" fill="var(--bar-blue)"/>
    <rect x="512" y="274" width="18" height="92" fill="var(--bar-blue)"/>
    <rect x="0" y="386" width="672" height="92" fill="url(#banner-fill)"/>
    <rect x="677" y="386" width="7" height="92" fill="var(--bar-blue)"/>
    <rect x="689" y="386" width="20" height="92" fill="var(--bar-blue)"/>

    <polyline points="800,512 562,512 562,560" fill="none" stroke="var(--brand-green)" stroke-width="2.5" stroke-dasharray="10 6"/>
    <circle cx="568" cy="692" r="129" fill="none" stroke="var(--brand-green)" stroke-width="2.5" stroke-dasharray="10 6"/>
    <circle cx="568" cy="692" r="119" fill="url(#photo-aed)" role="img" aria-label="Photo: rescuer applying AED pads to a person lying on a concrete floor"/>

    <path d="M272,560 H414 V628 H314 L300,656 L298,628 H272 Z" fill="var(--brand-green)"/>

    <circle cx="246" cy="834" r="130" fill="none" stroke="var(--ring-teal)" stroke-width="2.5" stroke-dasharray="10 6"/>
    <circle cx="246" cy="834" r="120" fill="url(#photo-cpr)" role="img" aria-label="Photo: instructor performing chest compressions on a person lying on pavement"/>
    <polyline points="242,966 242,1018 800,1018" fill="none" stroke="var(--ring-teal)" stroke-width="2.5" stroke-dasharray="10 6"/>

    <path d="M476,916 H500 L502,888 L516,916 H620 V984 H476 Z" fill="var(--tag-teal)"/>

    <circle cx="150" cy="1108" r="108" fill="var(--brand-blue)"/>
    <g class="camera-icon" fill="#ffffff">
      <rect x="136" y="1048" width="28" height="20" rx="3"/>
      <rect x="143" y="1044" width="10" height="5" rx="1"/>
      <circle cx="150" cy="1058" r="6.5" fill="var(--brand-blue)"/>
      <circle cx="150" cy="1058" r="4"/>
    </g>
  </svg>

  <h1 class="brand-name"><span class="line1">SUMMIT READINESS</span><span class="line2">ACADEMY, INC.</span></h1>
  <p class="tagline">CPR and First Aid Classes</p>
  <p class="cities">Sacramento | Stockton | Modesto</p>

  <p class="banner-text banner-weekly">WEEKY CLASSES</p>
  <p class="banner-text banner-firefighters">TAUGHT BY FIREFIGHTERS</p>

  <p class="price-tag price-bls">BLS - $49</p>
  <p class="price-tag price-cpr">CPR - $39</p>

  <p class="snap-note">snap a picture<br>of me for later</p>

  <dl class="contact">
    <dt>Phone</dt><dd>| 916-784-3126</dd>
    <dt>Website</dt><dd>| www.BlueRiverSkills.example</dd>
  </dl>
</main>
</body>
</html>
```